business card for make-up artist

I want an upscale looking business card to promote my business. I am a make up artist/hair stylist.
I want to use the words "Velvet Hour" as the name of my business. I'm not sure of a good tag line to go under that, so any suggestions are welcomed. If there are different styles instead of just using the same kind of normal shape business card i am open to that as well.
I like the font that is seen on Mirabel Journal.
My Name is Tessa Brantwood
my phone number is 418-305-7826
Instagram: the.velvet.hour

Industry/Entity Type

Hair And Beauty

Contact Information for Business Card

Name of Business: Velvet Hour
Licensed Cosmetologist Tessa Brantwood
418-305-7826

Font styles to use
Serif

Requirements
Must have
• I want an chic style business card. I love gold letters and maybe a black background. I like the font that is used in Mirabel Journal for their name Mirabel.
• FONT!! I LOVE the font called Onyx, Cheddar Jack, and Daydreamer that you can see an example on typeharbor.com
Should not have
• Cartoon characters

```html
<!DOCTYPE html>
<html lang="en">
<head>
<meta charset="utf-8">
<title>Velvet Hour — Business Card</title>
<link rel="stylesheet" href="https://fonts.googleapis.com/css2?family=Cormorant+Garamond:ital,wght@0,400;0,500;1,400&family=Playfair+Display:wght@400&display=swap">
<style>
  :root {
    --stage-center: #3a3532;
    --stage-edge: #0f0d0c;
    --card-black: #141213;
    --card-deep: #0a0909;
    --gold: #c9a24a;
    --gold-line: #d9b15a;
    --ivory: #f1ece4;
    --photo-warm: #8a6a3c;
    --photo-light: #d9c3a0;
    --photo-dark: #2a1d12;
  }
  * { margin: 0; padding: 0; box-sizing: border-box; }
  html, body { width: 841px; height: 1200px; overflow: hidden; }
  body {
    position: relative;
    background: radial-gradient(ellipse at 50% 40%, var(--stage-center) 0%, #1e1b19 55%, var(--stage-edge) 100%);
    font-family: "Cormorant Garamond", Georgia, serif;
    color: var(--ivory);
  }

  .card {
    position: absolute;
    left: 160px;
    width: 513px;
    background: radial-gradient(ellipse at 50% 50%, #201d1d 0%, var(--card-black) 55%, var(--card-deep) 100%);
    box-shadow: 0 18px 40px rgba(0,0,0,.6);
    overflow: hidden;
  }

  /* Front */
  .card--front { top: 112px; height: 294px; }
  .card__photo {
    height: 216px;
    background: linear-gradient(110deg, var(--photo-dark) 0%, var(--photo-warm) 30%, var(--photo-light) 60%, var(--photo-warm) 82%, var(--photo-dark) 100%);
  }
  .card__rule { height: 4px; background: var(--gold-line); }
  .card__footer {
    height: 74px;
    display: flex;
    align-items: center;
    justify-content: space-between;
    padding: 0 26px 0 24px;
  }
  .brand-small {
    font-family: "Playfair Display", Georgia, serif;
    font-size: 25px;
    line-height: 1;
    color: var(--gold);
    letter-spacing: 1px;
    text-transform: uppercase;
  }
  .handle {
    display: flex;
    align-items: center;
    gap: 9px;
    font-size: 15px;
    font-style: italic;
    color: var(--ivory);
  }
  .handle__dot {
    width: 11px; height: 11px;
    border: 1.5px solid var(--ivory);
    border-radius: 50%;
  }

  /* Back */
  .card--back {
    top: 550px; height: 327px;
    text-align: center;
  }
  .back__lines {
    margin-top: 48px;
    font-size: 32px;
    line-height: 46px;
    color: var(--ivory);
  }
  .back__contact {
    margin-top: 16px;
    font-size: 21px;
    font-style: italic;
    line-height: 34px;
    color: var(--gold);
  }
  .contact-row { display: flex; justify-content: center; align-items: center; gap: 10px; }
  .contact-row svg { width: 16px; height: 16px; }
  .contact-row .handle__dot { border-color: var(--gold); width: 13px; height: 13px; }
  .back__services {
    margin-top: 22px;
    font-size: 13px;
    letter-spacing: 1.5px;
    text-transform: uppercase;
    color: var(--ivory);
    word-spacing: 4px;
  }

  /* Standalone wordmark */
  .brand-large {
    position: absolute;
    top: 990px;
    left: 0; width: 841px;
    text-align: center;
    font-family: "Playfair Display", Georgia, serif;
    font-size: 72px;
    line-height: 1;
    color: var(--gold);
    letter-spacing: 3px;
    text-transform: uppercase;
  }
</style>
</head>
<body>
  <section class="card card--front">
    <div class="card__photo" role="img" aria-label="Editorial beauty portrait with dramatic gold styling and jewellery"></div>
    <div class="card__rule"></div>
    <div class="card__footer">
      <span class="brand-small">Velvet Hour</span>
      <span class="handle"><span class="handle__dot"></span>the.velvet.hour</span>
    </div>
  </section>

  <section class="card card--back">
    <div class="back__lines">
      <p>Velvet Hour</p>
      <p>Licensed Cosmetologist</p>
      <p>Tessa Brantwood</p>
    </div>
    <div class="back__contact">
      <p class="contact-row">
        <svg viewBox="0 0 24 24" aria-hidden="true"><path fill="#c9a24a" d="M6.6 10.8a15.1 15.1 0 0 0 6.6 6.6l2.2-2.2a1 1 0 0 1 1-.25 11.4 11.4 0 0 0 3.6.57 1 1 0 0 1 1 1V20a1 1 0 0 1-1 1A17 17 0 0 1 3 4a1 1 0 0 1 1-1h3.5a1 1 0 0 1 1 1c0 1.25.2 2.45.57 3.57a1 1 0 0 1-.25 1z"/></svg>
        418-305-7826
      </p>
      <p class="contact-row"><span class="handle__dot"></span>the.velvet.hour</p>
    </div>
    <p class="back__services">Make up artist &nbsp; Hair stylist</p>
  </section>

  <div class="brand-large">Velvet Hour</div>
</body>
</html>
```